IT Security Company Website

We would like to create a new look for our current company site veltrom.io. The company offercyber security services for banks, goverment etc. Therefore a very professional look is important. We need at least 2 pages designed.

Target Market(s)

B2B

Coding

Coded - Design and coding required

Number of Pages Required

1 page

```html
<!DOCTYPE html>
<html lang="en">
<head>
<meta charset="utf-8">
<title>Veltrom – Defend Against Cyber Attacks</title>
<link href="https://fonts.googleapis.com/css2?family=Poppins:wght@400;500;600;700&family=Raleway:wght@300;400&display=swap" rel="stylesheet">
<style>
:root{
  --yellow:#ecc44a;
  --yellow-dark:#d9ad2a;
  --olive:#8c7a3a;
  --ink:#1f1f24;
  --text:#333338;
  --grey-bg:#f1f2f4;
  --white:#ffffff;
  --footer:#1f1f25;
  --cream:#f7e9bd;
}
*{box-sizing:border-box;margin:0;padding:0}
html,body{width:1200px;height:5164px;overflow:hidden}
body{font-family:"Poppins",sans-serif;color:var(--text);background:var(--white);position:relative}
.abs{position:absolute}
.logo{font-family:"Raleway",sans-serif;font-weight:300;letter-spacing:2px;color:var(--ink)}
.nav{top:48px;left:566px;display:flex;gap:32px;font-size:13px;font-weight:500;color:var(--ink)}
.nav .active{color:var(--yellow)}
.btn{display:flex;align-items:center;justify-content:center;border-radius:30px;font-weight:600;font-size:21px}
.btn-yellow{background:var(--yellow);color:var(--white)}
.btn-outline{border:2px solid var(--ink);color:var(--ink);background:var(--white)}
.hl{color:var(--yellow)}
.title{font-weight:700;color:var(--ink)}
.para{font-size:16px;line-height:32px;color:var(--text)}
.card{background:var(--white);border-radius:18px;box-shadow:0 4px 14px rgba(0,0,0,.08);text-align:center;padding:0 26px;overflow:hidden}
.card h3{font-size:21px;line-height:27px;font-weight:600;color:var(--ink);margin-top:112px}
.card p{font-size:13.5px;line-height:26px;margin-top:8px}
.card .icon{position:absolute;top:24px;left:50%;margin-left:-36px;width:72px;height:72px}
.card .go{position:absolute;right:0;bottom:0;width:60px;height:56px;background:var(--yellow);border-radius:18px 0 18px 0;color:var(--white);font-weight:700;font-size:20px;display:flex;align-items:center;justify-content:center}
.news .img{height:240px;border-radius:14px;position:relative}
.news .date{position:absolute;top:14px;left:18px;color:var(--white);font-size:13px;font-weight:600}
.news h4{font-size:22px;line-height:34px;font-weight:600;color:var(--ink);margin-top:26px}
.news a{display:block;margin-top:10px;font-size:14px;color:var(--yellow);text-decoration:underline}
.footer-col h5{font-size:22px;font-weight:600;color:var(--yellow);margin-bottom:16px}
.footer-col li{list-style:none;font-size:14px;color:var(--white);line-height:36px}
.hero-text{z-index:2}
</style>
</head>
<body>

<!-- Header -->
<div class="abs logo" style="top:22px;left:72px;font-size:62px">VELTROM</div>
<nav class="abs nav">
  <span class="active">HOME</span><span>Q&amp;A</span><span>PRICING</span><span>ABOUT US</span><span>CONTACT</span><span>RESOURCES</span>
</nav>

<!-- Hero -->
<div class="abs" role="img" aria-label="Illustration of a hooded hacker at a computer screen showing an attack warning, with globe and padlock shapes"
  style="left:620px;top:140px;width:580px;height:700px;background:linear-gradient(160deg,#a8954f 0%,#8c7a3a 55%,#e9c650 100%);border-radius:260px 0 0 320px"></div>
<h1 class="abs title hero-text" style="top:262px;left:74px;font-size:48px;line-height:50px;color:var(--yellow)">Defend Against<br>Cyber</h1>
<h2 class="abs title hero-text" style="top:374px;left:74px;font-size:30px">Attacks Before They Happen</h2>
<p class="abs para hero-text" style="top:426px;left:74px;width:510px">Veltrom helps you understand when, where and how stolen or accidentally leaked information in dark web markets, forums, botnet logs, IRC, social media and other sources is exposed.</p>
<div class="abs btn btn-yellow" style="top:592px;left:74px;width:190px;height:60px">Learn More</div>
<div class="abs btn btn-outline" style="top:592px;left:286px;width:236px;height:60px">Request Demo</div>

<!-- CISO solution -->
<div class="abs" role="img" aria-label="Illustration of a thoughtful man in a suit standing at the centre of a maze"
  style="left:74px;top:940px;width:510px;height:470px;background:radial-gradient(ellipse at 50% 45%,var(--cream) 0 60%,transparent 61%)"></div>
<h2 class="abs title" style="top:970px;left:614px;font-size:38px;line-height:46px"><span class="hl">The CISO’s Solution</span> –<br>forewarned is forearmed.</h2>
<p class="abs para" style="top:1080px;left:614px;width:520px">Veltrom helps you understand when, where and how stolen or accidentally leaked information is exposed. Veltrom’s alerting service can also detect threats before they turn into incidents. There are certain indicators that can be measured. Before an attack takes place, hackers often reserve similar domain names (typosquatting), they spoof profiles in social media like Linkwork or they exchange information about targets in hacker forums.</p>
<div class="abs btn btn-yellow" style="top:1366px;left:614px;width:198px;height:58px">Learn More</div>

<!-- Grey section with wave -->
<div class="abs" style="top:1600px;left:0;width:1200px;height:2380px;background:var(--grey-bg)"></div>
<svg class="abs" style="top:1530px;left:0" width="1200" height="140" viewBox="0 0 1200 140">
  <path d="M0 40 C300 10 500 110 800 70 C1000 40 1100 40 1200 60 L1200 140 L0 140Z" fill="var(--yellow)"/>
  <path d="M0 90 C300 60 500 140 800 100 C1000 75 1100 80 1200 90 L1200 140 L0 140Z" fill="var(--grey-bg)"/>
</svg>

<h2 class="abs title" style="top:1680px;left:0;width:1200px;text-align:center;font-size:38px;line-height:46px"><span class="hl">The CISO’s Solution</span> –<br>forewarned is forearmed.</h2>

<svg width="0" height="0" style="position:absolute">
  <symbol id="ic-screen" viewBox="0 0 72 72"><rect x="6" y="14" width="60" height="38" rx="3" fill="none" stroke="#d9ad2a" stroke-width="2.5"/><rect x="28" y="52" width="16" height="8" fill="#d9ad2a"/><circle cx="36" cy="33" r="7" fill="none" stroke="#d9ad2a" stroke-width="2.5"/></symbol>
  <symbol id="ic-lock" viewBox="0 0 72 72"><rect x="18" y="32" width="36" height="30" rx="4" fill="none" stroke="#d9ad2a" stroke-width="2.5"/><path d="M26 32 V22 a10 10 0 0 1 20 0 V32" fill="none" stroke="#d9ad2a" stroke-width="2.5"/><circle cx="36" cy="46" r="4" fill="#d9ad2a"/></symbol>
  <symbol id="ic-mail" viewBox="0 0 72 72"><rect x="8" y="20" width="56" height="36" rx="3" fill="none" stroke="#d9ad2a" stroke-width="2.5"/><path d="M8 22 L36 42 L64 22" fill="none" stroke="#d9ad2a" stroke-width="2.5"/></symbol>
  <symbol id="ic-people" viewBox="0 0 72 72"><circle cx="24" cy="24" r="7" fill="none" stroke="#d9ad2a" stroke-width="2.5"/><circle cx="48" cy="24" r="7" fill="none" stroke="#d9ad2a" stroke-width="2.5"/><path d="M12 56 a12 12 0 0 1 24 0 M36 56 a12 12 0 0 1 24 0" fill="none" stroke="#d9ad2a" stroke-width="2.5"/></symbol>
</svg>

<div class="abs card" style="top:1824px;left:74px;width:328px;height:326px"><svg class="icon"><use href="#ic-screen"/></svg><h3>Prevent Phishing</h3><p>We monitor all new domain registrations (ccTLDs, gTLDs, uTLD, sTLD). In doing so, we also record typical typosquatting techniques.</p><div class="go">»</div></div>
<div class="abs card" style="top:1824px;left:436px;width:328px;height:326px"><svg class="icon"><use href="#ic-lock"/></svg><h3>Detect<br>exposed infrastructure</h3><p>We monitor server access, IOT (Scanbase) or complete DB dumps in different formats (CSV, Memory Dumps, Office Files etc).</p><div class="go">»</div></div>
<div class="abs card" style="top:1824px;left:796px;width:328px;height:326px"><svg class="icon"><use href="#ic-lock"/></svg><h3>Detect leaks from<br>ransomware</h3><p>In ransomware attacks, victims are blackmailed into paying a ransom sum in order to regain access to their own data.</p><div class="go">»</div></div>
<div class="abs card" style="top:2184px;left:74px;width:328px;height:326px"><svg class="icon"><use href="#ic-screen"/></svg><h3>Find exposed data in<br>the darknet</h3><p>Monitoring whether your organisation’s name appears in Dark Web forums, Onion-, I2P and paste sites.</p><div class="go">»</div></div>
<div class="abs card" style="top:2184px;left:436px;width:328px;height:326px"><svg class="icon"><use href="#ic-mail"/></svg><h3>Detect spoofing and<br>impersonation</h3><p>We monitor social media services such as Chirpnet, Threadly, Vidstream, Pulsechat, etc. for posts that could be damaging.</p><div class="go">»</div></div>
<div class="abs card" style="top:2184px;left:796px;width:328px;height:326px"><svg class="icon"><use href="#ic-people"/></svg><h3>Understand employee<br>exposure</h3><p>Employees who are heavily exposed to the Internet are at greater risk of social engineering attacks such as phishing.</p><div class="go">»</div></div>

<div class="abs btn btn-yellow" style="top:2572px;left:500px;width:198px;height:58px">Learn More</div>

<!-- Video -->
<h2 class="abs title" style="top:2704px;left:0;width:1200px;text-align:center;font-size:38px"><span class="hl">Watch</span> a Video</h2>
<div class="abs" role="img" aria-label="Video still of gloved hands typing on a laptop in the dark"
  style="top:2788px;left:164px;width:870px;height:500px;border:4px solid var(--yellow);border-radius:18px;background:radial-gradient(ellipse at 45% 35%,#4a4d55 0,#222328 55%,#141418 100%);box-shadow:0 10px 20px rgba(0,0,0,.15)"></div>
<svg class="abs" style="top:2974px;left:535px" width="130" height="130" viewBox="0 0 130 130">
  <circle cx="65" cy="65" r="60" fill="#8c7a3a"/><circle cx="65" cy="65" r="46" fill="none" stroke="#fff" stroke-width="7"/><path d="M52 40 L92 65 L52 90Z" fill="#fff"/>
</svg>

<!-- News -->
<h2 class="abs title" style="top:3366px;left:0;width:1200px;text-align:center;font-size:38px"><span class="hl">Latest</span> News</h2>
<svg class="abs" style="top:3620px;left:42px" width="20" height="34" viewBox="0 0 20 34"><path d="M17 2 L3 17 L17 32" fill="none" stroke="#777" stroke-width="2.5"/></svg>
<svg class="abs" style="top:3620px;left:1138px" width="20" height="34" viewBox="0 0 20 34"><path d="M3 2 L17 17 L3 32" fill="none" stroke="#777" stroke-width="2.5"/></svg>
<div class="abs news" style="top:3456px;left:74px;width:328px"><div class="img" role="img" aria-label="Photo of hands on a keyboard with a glowing padlock" style="background:linear-gradient(135deg,#0b2a4a,#1f6fb2)"><span class="date">July 04, 2022</span></div><h4>QK3 banking solution hacked, data leaked online</h4><a>Read More</a></div>
<div class="abs news" style="top:3456px;left:436px;width:328px"><div class="img" role="img" aria-label="Photo of rows of security cameras on a wall" style="background:linear-gradient(135deg,#4b4e52,#2a2c30)"><span class="date">July 04, 2022</span></div><h4>Norvanta experienced a cyber attack</h4><a>Read More</a></div>
<div class="abs news" style="top:3456px;left:796px;width:328px"><div class="img" role="img" aria-label="Photo of a hooded figure at a desk in a dark blue room" style="background:radial-gradient(circle at 60% 30%,#1b7fa0,#07202c 70%)"><span class="date">July 04, 2022</span></div><h4>Vexlock Ransomware back online, 21 victims in a month</h4><a>Read More</a></div>

<!-- Demo -->
<svg class="abs" style="top:3940px;left:0" width="1200" height="640" viewBox="0 0 1200 640">
  <defs><linearGradient id="demoBg" x1="0" y1="0" x2="1" y2="1"><stop offset="0" stop-color="#4a4b50"/><stop offset="1" stop-color="#2e2f34"/></linearGradient></defs>
  <path d="M0 30 C300 0 600 70 900 40 C1050 25 1150 20 1200 30 L1200 610 C900 560 500 640 0 560Z" fill="url(#demoBg)"/>
  <path d="M0 30 C300 0 600 70 900 40 C1050 25 1150 20 1200 30 L1200 70 C1000 60 800 110 500 90 C300 75 100 60 0 80Z" fill="var(--yellow)"/>
  <path d="M0 520 C400 600 800 520 1200 570 L1200 620 C800 580 400 660 0 580Z" fill="var(--yellow)"/>
</svg>
<h2 class="abs" style="top:4094px;left:0;width:1200px;text-align:center;font-size:38px;font-weight:600;color:var(--white)">Arrange a live demo today!</h2>
<div class="abs" style="top:4170px;left:164px;width:870px;height:60px;border-radius:30px;background:var(--white);padding-left:30px;display:flex;align-items:center;font-size:16px;color:var(--ink)">Enter Email Address</div>
<div class="abs" style="top:4254px;left:0;width:1200px;display:flex;justify-content:center;align-items:center;gap:10px;font-size:14px;color:var(--white)"><span style="width:14px;height:14px;border:1px solid #fff;display:inline-block"></span>I agree that my data is stored for the purpose of a live demo</div>
<div class="abs btn btn-yellow" style="top:4292px;left:164px;width:870px;height:58px;font-size:22px">Submit</div>

<!-- Sign up -->
<h2 class="abs title" style="top:4618px;left:112px;font-size:38px;line-height:44px">Sign Up For Cyber Threat<br>Intelligence Alerts</h2>
<svg class="abs" style="top:4640px;left:480px" width="380" height="100" viewBox="0 0 380 100">
  <path d="M0 60 C80 80 140 40 120 30 C100 20 110 55 170 55 C230 55 280 40 320 50" fill="none" stroke="#888" stroke-width="1.5" stroke-dasharray="6 5"/>
  <path d="M300 40 L376 14 L330 70 L322 50Z" fill="none" stroke="#555" stroke-width="1.8"/>
</svg>
<div class="abs btn btn-yellow" style="top:4626px;left:866px;width:222px;height:60px">Sign Up Now</div>

<!-- Footer -->
<footer class="abs" style="top:4790px;left:0;width:1200px;height:374px;background:var(--footer)">
  <div class="abs logo" style="top:150px;left:72px;font-size:56px;color:var(--white)">VELTROM</div>
  <div class="abs" style="top:226px;left:74px;font-size:13px;line-height:20px;color:var(--white)">Copyright ©2022 Veltrom<br>All Right Reserved</div>
  <div class="abs footer-col" style="top:64px;left:378px"><h5>Links</h5><ul><li>Home</li><li>Q&amp;A</li><li>Pricing</li><li>About us</li><li>Contact</li><li>Resources</li></ul></div>
  <div class="abs footer-col" style="top:64px;left:616px"><h5>Resources</h5><ul><li>Screenshots</li><li>News</li><li>Partner Program</li><li>Wiki</li><li>References</li><li>In the Press</li></ul></div>
  <div class="abs footer-col" style="top:64px;left:898px"><h5>Get in Touch</h5><ul><li>Facenote</li><li>Chirpnet</li><li>Snapgram</li><li>Linkwork</li><li>Vidstream</li></ul></div>
</footer>

</body>
</html>
```